High end, luxury real estate property brochure

I need to have a property Brochure with 10-15 pages that will allow me to enter 30-40 photos and content about the home. It needs to be very high end and able to be edited in either word or publisher. I want to be able to use the pages individually when appropriate and then all together for larger homes. I need the template back by early Wednesday morning. Ideally, the brochure will be like a small booklet with a place for photos and content on the front and back of the pages. I need to add my company's logo and my photo to the project along with our office address etc..
Updates

Project Deadline Extended
Reason: I have decided to purchase more than one design and want to extend time for additional submissions.

Target Market(s)

Home Buyers in the Midwest (Indiana)

Industry/Entity Type

Real Estate Agent

Font styles to use
Serif

Requirements
Must have
• Graphically appealing. Integrated look between the pages. Several places for me to add photos of different sizes to highlight the homes features. The ability for me to change font, font colors, background colors, etc... Must have a high end, luxury feel. I will be adding descriptions and content about the photos so I need areas to add that information. I want the project to be able to be printed as a booklet for larger homes and to be able to use parts of the brochure for smaller homes as I won't have as many photos. Resolution must be fantastic. Clean lines.
Nice to have
• I am with Brantford Osgood Realty and our colors our logo is red so many of our publications are in Black and red. Dorian Fairbrook Promo Studios is a program that has some high end marketing pieces and designs that I like. I prefer the designs in the slate and black colors.
Should not have
• Cartoons graphics, pastel colors, "busy" designs.

```html
<!DOCTYPE html>
<html lang="en">
<head>
<meta charset="utf-8">
<title>Brantford Osgood Realty – Luxury Property Brochure</title>
<link rel="stylesheet" href="https://fonts.googleapis.com/css2?family=Arimo:wght@400;700&display=swap">
<style>
  :root{
    --backdrop:#e9e9e9;
    --ink:#050505;
    --paper:#ffffff;
    --slate:#565656;
    --brand-red:#b5121b;
    --text-light:#f1f1f1;
    --text-dark:#2a2a2a;
    --dusk:linear-gradient(160deg,#1c3f86 0%,#3a5fa8 45%,#c79a55 75%,#2a3a5c 100%);
    --garden:linear-gradient(160deg,#7f9e63 0%,#dfe3dc 45%,#5f7f44 100%);
    --interior:linear-gradient(150deg,#f2f0ec 0%,#c9c2b8 55%,#6d655d 100%);
    --warm-room:linear-gradient(150deg,#e9cfa8 0%,#a8754a 55%,#5a3a24 100%);
    --sunset:linear-gradient(170deg,#c98a93 0%,#6e7b5a 45%,#3b4a2c 100%);
    --night:linear-gradient(170deg,#15264a 0%,#2c3e6a 50%,#c8964f 80%,#1a2238 100%);
    --plan:linear-gradient(180deg,#fafafa,#ececec);
  }
  *{box-sizing:border-box;margin:0;padding:0}
  html,body{width:1200px;height:1200px;overflow:hidden}
  body{background:var(--backdrop);font-family:"Arimo",Arial,sans-serif;position:relative}

  .photo{width:100%;height:100%}
  .photo--dusk{background:var(--dusk)}
  .photo--garden{background:var(--garden)}
  .photo--interior{background:var(--interior)}
  .photo--warm{background:var(--warm-room)}
  .photo--sunset{background:var(--sunset)}
  .photo--night{background:var(--night)}
  .photo--plan{background:var(--plan)}

  /* covers */
  .cover{position:absolute;width:297px;height:420px;background:var(--ink);display:flex;box-shadow:0 2px 6px rgba(0,0,0,.25)}
  .cover--front{left:37px;top:52px}
  .cover--back{left:350px;top:102px}
  .cover__strip{width:108px;height:100%;position:relative;color:var(--text-light)}
  .cover__photo{flex:1}
  .cover-brand{display:flex;align-items:center;gap:5px;font-weight:700;font-size:10px;line-height:1.15;color:var(--paper)}
  .cover-brand__mark{width:9px;height:9px;background:var(--paper);flex:none}
  .cover--front .cover-brand{position:absolute;left:14px;top:20px;width:86px}
  .cover--back .cover__strip{width:108px}
  .agent-portrait{position:absolute;left:40px;top:18px;width:50px;height:62px;background:linear-gradient(180deg,#e4e4e4,#9a9a9a)}
  .agent-name{position:absolute;left:40px;top:86px;font-size:4.5px;letter-spacing:.3px}
  .agent-phone,.agent-address{position:absolute;left:40px;display:flex;align-items:center;gap:3px;font-size:4.5px}
  .agent-phone{top:96px;left:50px}
  .cover--back .cover-brand{position:absolute;left:18px;top:355px;width:86px}
  .agent-address{top:385px;left:18px;line-height:1.6;display:block}
  .agent-address span{display:flex;gap:3px;align-items:center}

  /* inside pages */
  .page{background:var(--ink);padding:12px;display:flex;flex-direction:column}
  .page__header{height:20px;background:var(--paper);position:relative;display:flex;align-items:center;flex:none;margin-bottom:4px}
  .page__header::after{content:"";position:absolute;left:calc(45% + 6px);bottom:-7px;border-left:8px solid transparent;border-right:8px solid transparent;border-top:7px solid var(--paper)}
  .header-brand{position:absolute;left:36%;display:flex;align-items:center;gap:3px;font-weight:700;font-size:6px;color:var(--brand-red);white-space:nowrap}
  .header-brand__mark{width:5px;height:5px;background:var(--brand-red)}
  .header-phone{position:absolute;right:8px;display:flex;align-items:center;gap:3px;font-size:5px;font-weight:700;color:var(--text-dark)}
  .page__body{flex:1;display:grid;gap:3px;min-height:0}
  .info{background:var(--slate);color:var(--text-light);padding:6px;font-size:4.3px;line-height:1.45;overflow:hidden}
  .info h3{font-size:4.6px;font-weight:700;margin-bottom:3px}
  .info ul{list-style:none;margin-bottom:5px}

  .spread{position:absolute;left:668px;width:498px;height:352px;display:flex;gap:4px;background:var(--ink);box-shadow:0 2px 6px rgba(0,0,0,.2)}
  .spread .page{flex:1}
  .spread--one{top:49px}
  .spread--two{top:424px}
  .spread--three{top:799px}

  .flyer{position:absolute;width:296px;height:420px;box-shadow:0 2px 6px rgba(0,0,0,.25)}
  .flyer--modern{left:37px;top:548px}
  .flyer--estate{left:350px;top:548px}
  .flyer .page__header{height:26px}
  .flyer .header-brand{font-size:7px}
  .flyer .info{font-size:5px;padding:8px}
  .flyer .info h3{font-size:5.4px}

  .a{grid-area:a}.b{grid-area:b}.c{grid-area:c}.d{grid-area:d}.e{grid-area:e}.f{grid-area:f}.g{grid-area:g}.h{grid-area:h}.p{grid-area:p}.s{grid-area:s}.t{grid-area:t}

  .layout-1l{grid-template:"a a" 1.25fr "b c" .8fr "b d" .65fr/1fr 1fr}
  .layout-1r{grid-template:"a a" 2fr "b t" 1fr/1.2fr .8fr}
  .layout-2l{grid-template:"a a" 1.7fr "p t" 1.05fr "p s" .5fr/1fr 1fr}
  .layout-2r{grid-template:"a h" 1fr "b h" 1fr "c h" 1fr/1.2fr .8fr}
  .layout-3l{grid-template:"a a" 1.4fr "b c" .8fr "t d" 1fr/1fr 1fr}
  .layout-3r{grid-template:"a t" 1.6fr "b c" .7fr "d e" .7fr/1.5fr 1fr}
  .layout-fm{grid-template:"a a" 1.6fr "b c" .75fr "d t" .75fr "e t" .75fr/.48fr .52fr}
  .layout-fe{grid-template:"a a a" 1.9fr "t t t" .75fr "b c d" .6fr "e f g" .6fr/1fr 1fr 1fr}
</style>
</head>
<body>

<svg width="0" height="0" style="position:absolute">
  <defs>
    <symbol id="icon-phone" viewBox="0 0 10 10"><circle cx="5" cy="5" r="4.3" fill="none" stroke="currentColor" stroke-width="1"/><path d="M3.4 2.8c.3-.3.6-.2.8.1l.5.8c.1.3 0 .5-.2.6l-.3.2c.3.7.8 1.2 1.5 1.5l.2-.3c.2-.2.4-.3.6-.2l.8.5c.3.2.4.5.1.8-.5.6-1.2.6-2 .1-1-.6-1.8-1.4-2.3-2.4-.3-.7-.2-1.2.3-1.7z" fill="currentColor"/></symbol>
    <symbol id="icon-pin" viewBox="0 0 10 10"><path d="M5 .8a3.2 3.2 0 0 0-3.2 3.2C1.8 6.4 5 9.4 5 9.4S8.2 6.4 8.2 4A3.2 3.2 0 0 0 5 .8zm0 4.4a1.2 1.2 0 1 1 0-2.4 1.2 1.2 0 0 1 0 2.4z" fill="currentColor"/></symbol>
  </defs>
</svg>

<!-- Front cover -->
<section class="cover cover--front">
  <div class="cover__strip">
    <div class="cover-brand"><span class="cover-brand__mark"></span>Brantford Osgood Realty</div>
  </div>
  <div class="cover__photo photo photo--dusk" role="img" aria-label="Modern stone and glass home at dusk with a lit pool"></div>
</section>

<!-- Back cover -->
<section class="cover cover--back">
  <div class="cover__photo photo photo--dusk" role="img" aria-label="Contemporary residence at twilight reflected in a pool"></div>
  <div class="cover__strip">
    <div class="agent-portrait" role="img" aria-label="Agent portrait placeholder"></div>
    <p class="agent-name">NAME XXXX XXXXX</p>
    <p class="agent-phone"><svg width="5" height="5"><use href="#icon-phone"/></svg>111 555 666</p>
    <div class="cover-brand"><span class="cover-brand__mark"></span>Brantford Osgood Realty</div>
    <div class="agent-address">
      <span><svg width="5" height="5"><use href="#icon-pin"/></svg>xxxxxxxxxxxxxxxx</span>
      <span style="padding-left:8px">xxxxxxxxxxxx</span>
    </div>
  </div>
</section>

<!-- Spread one -->
<section class="spread spread--one">
  <div class="page">
    <header class="page__header"><span class="header-brand"><span class="header-brand__mark"></span>Brantford Osgood Realty</span><span class="header-phone"><svg width="6" height="6"><use href="#icon-phone"/></svg>111 555 666</span></header>
    <div class="page__body layout-1l">
      <div class="a photo photo--garden" role="img" aria-label="Aerial view of a white estate among trees"></div>
      <div class="b photo photo--interior" role="img" aria-label="Double-height living room"></div>
      <div class="c photo photo--garden" role="img" aria-label="Rear garden and pool"></div>
      <div class="d photo photo--garden" role="img" aria-label="Gated driveway with palms"></div>
    </div>
  </div>
  <div class="page">
    <header class="page__header"><span class="header-brand"><span class="header-brand__mark"></span>Brantford Osgood Realty</span><span class="header-phone"><svg width="6" height="6"><use href="#icon-phone"/></svg>111 555 666</span></header>
    <div class="page__body layout-1r">
      <div class="a photo photo--interior" role="img" aria-label="Grand living room with fireplace"></div>
      <div class="b photo photo--garden" role="img" aria-label="Front facade with lawn"></div>
      <div class="t info"><h3>Property description</h3><p>A home of quiet distinction in a prime canyon setting, finished with care and ready for gracious daily living.</p></div>
    </div>
  </div>
</section>

<!-- Spread two -->
<section class="spread spread--two">
  <div class="page">
    <header class="page__header"><span class="header-brand"><span class="header-brand__mark"></span>Brantford Osgood Realty</span><span class="header-phone"><svg width="6" height="6"><use href="#icon-phone"/></svg>111 555 666</span></header>
    <div class="page__body layout-2l">
      <div class="a photo photo--garden" role="img" aria-label="White traditional house with front steps"></div>
      <div class="p photo photo--plan" role="img" aria-label="Floor plan"></div>
      <div class="t info"><h3>Property features</h3><p>This refined seven-bedroom residence pairs crafted detail with open living, a chef's kitchen, library, wine cellar and a sheltered garden terrace.</p></div>
      <div class="s photo photo--warm" role="img" aria-label="Dining room"></div>
    </div>
  </div>
  <div class="page">
    <header class="page__header"><span class="header-brand"><span class="header-brand__mark"></span>Brantford Osgood Realty</span><span class="header-phone"><svg width="6" height="6"><use href="#icon-phone"/></svg>111 555 666</span></header>
    <div class="page__body layout-2r">
      <div class="a photo photo--garden" role="img" aria-label="House seen from the drive"></div>
      <div class="b photo photo--garden" role="img" aria-label="Side elevation with lawn"></div>
      <div class="c photo photo--interior" role="img" aria-label="Breakfast room"></div>
      <div class="h photo photo--warm" role="img" aria-label="Entry hall with wood floor"></div>
    </div>
  </div>
</section>

<!-- Spread three -->
<section class="spread spread--three">
  <div class="page">
    <header class="page__header"><span class="header-brand"><span class="header-brand__mark"></span>Brantford Osgood Realty</span><span class="header-phone"><svg width="6" height="6"><use href="#icon-phone"/></svg>111 555 666</span></header>
    <div class="page__body layout-3l">
      <div class="a photo photo--garden" role="img" aria-label="Two-storey home with palm trees"></div>
      <div class="b photo photo--warm" role="img" aria-label="Living room with piano"></div>
      <div class="c photo photo--warm" role="img" aria-label="Beamed kitchen and dining"></div>
      <div class="t info"><h3>Property description</h3><p>Set in a gated neighborhood, this classic home offers four bedrooms, a guesthouse, mature landscaping and warm hardwood floors throughout.</p></div>
      <div class="d photo photo--interior" role="img" aria-label="Bedroom with canopy bed"></div>
    </div>
  </div>
  <div class="page">
    <header class="page__header"><span class="header-brand"><span class="header-brand__mark"></span>Brantford Osgood Realty</span><span class="header-phone"><svg width="6" height="6"><use href="#icon-phone"/></svg>111 555 666</span></header>
    <div class="page__body layout-3r">
      <div class="a photo photo--night" role="img" aria-label="Modern glass beach house at night"></div>
      <div class="t info"><h3>Property description</h3><p>Timeless modern living near the shore, with ocean views, clean lines, a glass stair and an open kitchen for entertaining.</p></div>
      <div class="b photo photo--warm" role="img" aria-label="Lounge with ocean view"></div>
      <div class="c photo photo--interior" role="img" aria-label="Open kitchen"></div>
      <div class="d photo photo--warm" role="img" aria-label="Staircase"></div>
      <div class="e photo photo--night" role="img" aria-label="Street view at night"></div>
    </div>
  </div>
</section>

<!-- Single flyer: modern home -->
<section class="flyer flyer--modern page">
  <header class="page__header"><span class="header-brand"><span class="header-brand__mark"></span>Brantford Osgood Realty</span><span class="header-phone"><svg width="7" height="7"><use href="#icon-phone"/></svg>111 555 666</span></header>
  <div class="page__body layout-fm">
    <div class="a photo photo--night" role="img" aria-label="White modern home with pool at dusk"></div>
    <div class="b photo photo--interior" role="img" aria-label="Living area"></div>
    <div class="c photo photo--night" role="img" aria-label="Lit facade and pool"></div>
    <div class="d photo photo--interior" role="img" aria-label="Dining room"></div>
    <div class="e photo photo--interior" role="img" aria-label="Kitchen"></div>
    <div class="t info">
      <h3>Property features</h3>
      <ul><li>- 8800 Square Feet Internal</li><li>- 42132 Square Feet Plot</li></ul>
      <h3>Property description</h3>
      <p>Situated at the end of a long gated drive, this modern glass home offers vast living areas, a media room, wine cellar and a pool pavilion.</p>
    </div>
  </div>
</section>

<!-- Single flyer: estate -->
<section class="flyer flyer--estate page">
  <header class="page__header"><span class="header-brand"><span class="header-brand__mark"></span>Brantford Osgood Realty</span><span class="header-phone"><svg width="7" height="7"><use href="#icon-phone"/></svg>111 555 666</span></header>
  <div class="page__body layout-fe">
    <div class="a photo photo--sunset" role="img" aria-label="Historic estate with stone pond at sunset"></div>
    <div class="t info"><h3>Property description</h3><p>One of the finest estates north of the boulevard, set on landscaped acres with a guesthouse, pools, waterfalls and a tennis court.</p></div>
    <div class="b photo photo--warm" role="img" aria-label="Arched doorway"></div>
    <div class="c photo photo--warm" role="img" aria-label="Library"></div>
    <div class="d photo photo--warm" role="img" aria-label="Great room"></div>
    <div class="e photo photo--garden" role="img" aria-label="Garden path"></div>
    <div class="f photo photo--warm" role="img" aria-label="Sitting room"></div>
    <div class="g photo photo--warm" role="img" aria-label="Formal dining room"></div>
  </div>
</section>

</body>
</html>
```